Need Power Point Presentation - That incorporates New Logo

We have a new logo and would like to incorporate it into a Power Point template. We are looking for title page, 2 body pages and a closing page design. If you have any questions please let me know. New logo is attached.

```html
<!DOCTYPE html>
<html lang="en">
<head>
<meta charset="utf-8">
<title>Presentation Title Slide</title>
<link href="https://fonts.googleapis.com/css2?family=Arimo:wght@400;700&display=swap" rel="stylesheet">
<style>
  :root {
    --page: #ffffff;
    --slide-light: #5c5c5c;
    --slide-dark: #000000;
    --side-panel: #242424;
    --footer-band: #3e3e3e;
    --text-white: #ffffff;
    --title-blue-top: #7fb2ee;
    --title-blue-bottom: #2f6cc4;
    --title-edge: #1b3f78;
    --brand-blue: #5ab4e4;
  }
  html, body {
    margin: 0;
    padding: 0;
    width: 1200px;
    height: 1000px;
    overflow: hidden;
    background: var(--page);
  }
  .slide {
    position: absolute;
    left: 128px;
    top: 125px;
    width: 960px;
    height: 720px;
    overflow: hidden;
    font-family: "Arimo", Arial, sans-serif;
  }
  .slide-art {
    position: absolute;
    inset: 0;
  }
  .subtitle {
    position: absolute;
    left: 55px;
    top: 162px;
    margin: 0;
    font-size: 25px;
    font-weight: 400;
    color: var(--text-white);
    letter-spacing: -0.2px;
  }
  .title {
    position: absolute;
    left: 50px;
    top: 232px;
    margin: 0;
    font-size: 60px;
    font-weight: 700;
    letter-spacing: 0.5px;
    line-height: 1;
    background: linear-gradient(180deg, var(--title-blue-top) 0%, var(--title-blue-bottom) 100%);
    -webkit-background-clip: text;
    background-clip: text;
    color: transparent;
    -webkit-text-stroke: 1px var(--title-edge);
    filter: drop-shadow(2px 3px 2px rgba(0,0,0,0.8));
  }
  .brand {
    position: absolute;
    right: 34px;
    bottom: 40px;
    display: flex;
    align-items: center;
    gap: 6px;
    color: var(--brand-blue);
    font-size: 21px;
    font-weight: 400;
    letter-spacing: 0.5px;
  }
  .brand-dot {
    width: 12px;
    height: 12px;
    border-radius: 50%;
    background: var(--brand-blue);
  }
</style>
</head>
<body>
  <section class="slide">
    <svg class="slide-art" width="960" height="720" viewBox="0 0 960 720" aria-hidden="true">
      <defs>
        <linearGradient id="side-fill" x1="0" y1="0" x2="1" y2="1">
          <stop offset="0" stop-color="#2e2e2e"/>
          <stop offset="1" stop-color="#1c1c1c"/>
        </linearGradient>
        <radialGradient id="main-fill" cx="0" cy="0" r="1.15" gradientUnits="objectBoundingBox">
          <stop offset="0" stop-color="var(--slide-light)"/>
          <stop offset="0.55" stop-color="#1e1e1e"/>
          <stop offset="1" stop-color="var(--slide-dark)"/>
        </radialGradient>
        <linearGradient id="band-fill" x1="0" y1="0" x2="1" y2="0">
          <stop offset="0" stop-color="#474747"/>
          <stop offset="1" stop-color="#3c3c3c"/>
        </linearGradient>
      </defs>
      <rect class="side-panel" width="960" height="720" fill="url(#side-fill)"/>
      <path class="main-sweep" d="M0,0 L642,0 C760,110 830,260 825,400 C820,560 760,660 672,720 L0,720 Z" fill="url(#main-fill)"/>
      <path class="footer-band" d="M0,675 C260,690 560,660 960,498 L960,720 L0,720 Z" fill="url(#band-fill)" opacity="0.96"/>
      <path class="sweep-edge" d="M642,0 C760,110 830,260 825,400 C820,560 760,660 672,720" fill="none" stroke="#111" stroke-opacity="0.5" stroke-width="1.5"/>
    </svg>
    <p class="subtitle">Sample Text</p>
    <h1 class="title">SAMPLE TEXT</h1>
    <div class="brand"><span class="brand-dot"></span><span class="brand-name">KELDRAN</span></div>
  </section>
</body>
</html>
```